Business Card Design Project

We need a business card design for a new company based in New York called "Marble Fox's". We do major installations of energy saving devices primarily LED lighting in large facilities. We would like a double sided card with our contact info on one side with our logo (to be designed) and on the other side the services we provide. We would like a heavy weight glossy card using the colors green and white. The final design should communicate environmental soundness and our market is very upscale corporations.
We would like our logo to illustrate LED lighting and we were thinking if we could get a stock picture of the Corliss Vane Building lit up on July 4th with red, white and blue LED lighting. The alternative would be anything that connotes environmentally proper thinking. It could be either a picture or a design.

```html
<!DOCTYPE html>
<html lang="en">
<head>
<meta charset="utf-8">
<title>Marble Fox's – Business Card</title>
<link rel="stylesheet" href="https://fonts.googleapis.com/css2?family=Roboto+Condensed:wght@400;500;700&display=swap">
<style>
  :root {
    --page-bg: #ece7df;
    --label-ink: #3b3631;
    --navy: #1b4291;
    --band-navy: #17428f;
    --white: #ffffff;
    --green-deep: #74bb1f;
    --green-mid: #a6d23a;
    --green-light: #eef46c;
  }
  * { margin: 0; padding: 0; box-sizing: border-box; }
  html, body {
    width: 1200px;
    height: 999px;
    overflow: hidden;
  }
  body {
    position: relative;
    background: var(--page-bg);
    font-family: "Roboto Condensed", "Arial Narrow", sans-serif;
  }
  .side-label {
    position: absolute;
    font-size: 34px;
    font-weight: 400;
    letter-spacing: 0.5px;
    color: var(--label-ink);
    line-height: 1;
  }
  .side-label--front { left: 122px; top: 450px; }
  .side-label--back { left: 995px; top: 904px; }

  .card {
    position: absolute;
    left: 236px;
    width: 727px;
    height: 415px;
    overflow: hidden;
  }
  .card--front {
    top: 64px;
    background: linear-gradient(225deg, var(--green-light) 0%, var(--green-mid) 40%, var(--green-deep) 75%, #8ac42a 100%);
  }
  .card--back {
    top: 520px;
    background: var(--white);
  }

  .wordmark {
    position: absolute;
    font-weight: 700;
    color: var(--navy);
    white-space: nowrap;
    line-height: 1;
    letter-spacing: -0.5px;
  }
  .card--front .wordmark {
    left: 0;
    right: 0;
    top: 174px;
    text-align: center;
    font-size: 62px;
  }
  .card--back .wordmark {
    left: 36px;
    top: 278px;
    font-size: 40px;
  }
  .website {
    position: absolute;
    left: 36px;
    top: 326px;
    font-size: 20px;
    font-weight: 500;
    color: var(--navy);
  }

  .contact {
    position: absolute;
    left: 368px;
    top: 62px;
    color: var(--navy);
  }
  .contact__name {
    font-size: 35px;
    font-weight: 500;
    line-height: 1.1;
  }
  .contact__title {
    font-size: 26px;
    font-weight: 400;
    line-height: 1.2;
  }
  .contact__details {
    margin-top: 46px;
    font-size: 23px;
    line-height: 31px;
  }
  .contact__email {
    margin-top: 18px;
    font-size: 23px;
  }

  .services {
    position: absolute;
    left: 0;
    right: 0;
    bottom: 0;
    height: 40px;
    background: var(--band-navy);
    color: var(--white);
    display: flex;
    align-items: center;
    justify-content: center;
    font-size: 19.5px;
    list-style: none;
  }
  .services li { padding: 0 11px; }
  .services li + li { border-left: 1.5px solid var(--white); line-height: 20px; }
</style>
</head>
<body>
  <span class="side-label side-label--front">FRONT</span>
  <section class="card card--front" aria-label="Card front">
    <div class="wordmark">Marble Fox's</div>
  </section>

  <section class="card card--back" aria-label="Card back">
    <div class="wordmark">Marble Fox's</div>
    <div class="website">www.marblefox.com</div>

    <div class="contact">
      <p class="contact__name">DANA WHITFIELD</p>
      <p class="contact__title">Sales Executive</p>
      <p class="contact__details">Address 1 Address 2, NY<br>000-0000-0000</p>
      <p class="contact__email">dana.whitfield@marblefox.com</p>
    </div>

    <ul class="services">
      <li>LED Lighting Installation</li>
      <li>Repair and Maintenance</li>
      <li>Quality Product Assurance</li>
    </ul>
  </section>
  <span class="side-label side-label--back">BACK</span>
</body>
</html>
```